Building Servicess

We need a new business card design for a company. We specialise in: Electrical/Site temporary electrics, Data/Network Installation, Passive Fire Protection

Industry/Entity Type

Construction

Contact Information for Business Card

Services provided as detailed on project description

Font styles to use
Serif

Colors
0054AA
0677BA
7BADD7
CADEEF
E8F1F8
00AB8E
00BBA5
67D7C9
C6EFE9
E9F9F6
EB3D1F
EC4F4E
F09395
F8D3D4
FCEDEE

Requirements
Must have
• Company logo-contact details-phone numbers

```html
<!DOCTYPE html>
<html lang="en">
<head>
<meta charset="utf-8">
<title>Brightwire Services – Business Card</title>
<link rel="stylesheet" href="https://fonts.googleapis.com/css2?family=Raleway:wght@700&family=Arimo:wght@400&display=swap">
<style>
  :root {
    --stage: #3d3d3d;
    --brand-blue: #0f76bc;
    --steel-grey: #808184;
    --light-grey: #d9dadb;
    --paper: #ffffff;
    --shadow: rgba(0,0,0,0.85);
  }
  * { margin: 0; padding: 0; box-sizing: border-box; }
  html, body { width: 1200px; height: 801px; overflow: hidden; }
  body { background: var(--stage); position: relative; font-family: "Arimo", Arial, sans-serif; }

  .card {
    position: absolute; top: 274px; width: 443px; height: 263px;
    overflow: hidden; box-shadow: 2px 2px 2px var(--shadow);
  }
  .card--front { left: 153px; background: var(--brand-blue); }
  .card--back { left: 625px; background: var(--paper); }

  .front-panel {
    position: absolute; left: 0; top: 0; width: 190px; height: 263px;
    background: linear-gradient(135deg, var(--steel-grey) 0%, var(--light-grey) 55%, var(--paper) 100%);
  }

  .holder { position: absolute; left: 226px; top: 75px; color: var(--paper); }
  .holder__name { font-family: "Raleway", Arial, sans-serif; font-weight: 700; font-size: 17px; letter-spacing: 0.2px; line-height: 1; }
  .holder__role { font-size: 12px; line-height: 1.1; margin-top: 2px; }

  .contact-list { position: absolute; left: 226px; top: 123px; list-style: none; color: var(--paper); font-size: 13px; }
  .contact-list li { display: flex; align-items: center; height: 15.6px; }
  .contact-list svg { width: 12px; height: 12px; margin-right: 6px; flex: none; }

  .brand { position: absolute; left: 0; right: 0; top: 100px; display: flex; justify-content: center; align-items: center; }
  .brand__square { width: 18px; height: 18px; background: var(--steel-grey); margin-right: 8px; }
  .brand__name { font-family: "Raleway", Arial, sans-serif; font-weight: 700; font-size: 22px; line-height: 1; color: var(--brand-blue); letter-spacing: 0.3px; }

  .divider { position: absolute; left: 0; top: 155px; width: 100%; height: 4px; background: var(--steel-grey); }
  .services { position: absolute; left: 0; top: 159px; width: 100%; height: 104px; background: var(--brand-blue); }
  .service { position: absolute; top: 19px; width: 160px; margin-left: -80px; text-align: center; color: var(--paper); font-size: 12px; line-height: 15px; }
  .service__icon { display: block; width: 41px; height: 38px; margin: 0 auto 5px; background: var(--paper); }
  .service__icon svg { width: 41px; height: 38px; }
  .service--electrical { left: 90px; }
  .service--network { left: 238px; }
  .service--fire { left: 363px; }
</style>
</head>
<body>

<section class="card card--front" aria-label="Card front">
  <div class="front-panel" role="img" aria-label="Decorative grey and white panel"></div>

  <div class="holder">
    <p class="holder__name">MAREK DOLAN</p>
    <p class="holder__role">Managing Director</p>
  </div>

  <ul class="contact-list">
    <li><svg viewBox="0 0 24 24"><path d="M6 2l4 4-2 3c1 3 4 6 7 7l3-2 4 4-3 4C10 22 2 14 2 5z" fill="none" stroke="#fff" stroke-width="2"/></svg>020 7946 0183</li>
    <li><svg viewBox="0 0 24 24"><rect x="6" y="2" width="12" height="20" rx="2" fill="none" stroke="#fff" stroke-width="2.5"/><circle cx="12" cy="18" r="1.3" fill="#fff"/></svg>07700900417</li>
    <li><svg viewBox="0 0 24 24"><rect x="1" y="5" width="22" height="14" fill="#fff"/><path d="M1 5l11 8 11-8" fill="none" stroke="var(--brand-blue)" stroke-width="1.5"/></svg>info@brightwireservices.com</li>
    <li><svg viewBox="0 0 24 24"><g fill="none" stroke="#fff" stroke-width="1.8"><circle cx="12" cy="12" r="10"/><ellipse cx="12" cy="12" rx="4.5" ry="10"/><path d="M2 12h20M4 7h16M4 17h16"/></g></svg>www.brightwireservices.com</li>
  </ul>
</section>

<section class="card card--back" aria-label="Card back">
  <div class="brand">
    <span class="brand__square" aria-hidden="true"></span>
    <p class="brand__name">BRIGHTWIRE SERVICES</p>
  </div>

  <div class="divider"></div>

  <div class="services">
    <div class="service service--electrical">
      <span class="service__icon"><svg viewBox="0 0 41 38" aria-hidden="true"><circle cx="18" cy="18" r="11" fill="none" stroke="var(--brand-blue)" stroke-width="2"/><path d="M27 8l-8 12h5l-6 14 12-17h-5l5-9z" fill="var(--brand-blue)"/></svg></span>
      ELECTRICAL/SITE<br>TEMPORARY ELECTRICS
    </div>
    <div class="service service--network">
      <span class="service__icon"><svg viewBox="0 0 41 38" aria-hidden="true"><g fill="none" stroke="var(--brand-blue)" stroke-width="1.5"><rect x="16" y="6" width="9" height="7"/><path d="M20.5 13v5M9 18h23M13 18v4M28 18v4"/><rect x="8" y="22" width="9" height="7"/><rect x="24" y="22" width="9" height="7"/></g></svg></span>
      DATA/NETWORK<br>INSTALLATION
    </div>
    <div class="service service--fire">
      <span class="service__icon"><svg viewBox="0 0 41 38" aria-hidden="true"><path d="M20.5 4l12 4v10c0 8-6 13-12 16-6-3-12-8-12-16V8z" fill="var(--brand-blue)"/><path d="M20.5 12c4 4 6 7 5 11-1 3-3 4-5 4s-5-2-5-5c0-2 1-3 2-4 0 2 1 3 2 3-1-3 0-6 1-9z" fill="#fff"/></svg></span>
      PASSIVE FIRE<br>PROTECTION
    </div>
  </div>
</section>

</body>
</html>
```